Business Card design project for new family-run construction business

We need a logo and business card designed for a new construction company. We want to convey a professional, but approachable image. We hope to be servicing small residential clients as well as large commercial contracts as well.
Our business will employ a single "Hydro excavator" truck, which can be used for multiple purposes: vacuuming up dirt or water, digging holes, clearing sewer blockages and so on.
We are open to different colour schemes, however blue and white, or yellow/green would be good combinations. We are open to multiple colours (2-4), so long as they are complimentary.

EDIT: Let's not put much emphasis on the octopus... unless it's very clear that the arms are actual vacuum hoses, it won't make sense. An octopus on it's own has little to do with our business.

Please also do not use actual photos of hydro-vac trucks. This is not the aesthetic we are going for.

**The logo should instead be: A stylized outline of a hydrovac truck (a line drawing or digital version of a line-drawing). See the two examples in the attached images of hydrovac trucks. I've also included a very crude pen outline as a reference. Please use your artistic discretion and talent (as I clearly have none) to make something that looks much nicer. Thanks for your efforts!**

The front of the card should have the following elements:
Logo
Name: P & K Hydro Excavation and Flushign
Two phone numbers: Direct and Office
Email address
Website
It should also have the name of the employee and their job title
At the bottom of the card it should say (in a noticeable way): "24/7 Emergency Calls Welcome"

The back of the card should have the following elements:
"20 Years Experience"
"A Canadian Family Run Business"
A small maple-leaf logo that is in a similar style to the rest of the card/logos in the bottom right corner of the back of the card. (see attached)

**We have just added a number of business card designs that really appeal to us to offer inspiration.**

Reason: We have not received designs that hit the mark of what we are looking for. Feedback has been posted, so we would like to provide the designers more time.

Target Market(s)

Commercial and residential customers. As big as large malls and office buildings, as small single-family home owners

Industry/Entity Type

Construction Company

Contact Information for Business Card

We have just added a number of business card designs that really appeal to us to offer inspiration.

Logo
Email address
Website

"20 Years Experience"

Logo Text

P & K Hydro Excavation and Flushing

Font styles to use
Serif
Sans Serif
Other font styles liked:
• Helvetica, Futura, Impact, bold strong, modern fonts that convey a sense of design and style

Colors
0592cd
ec1f27
9bcb3c

Requirements
Must have
• The front of the card should have the following elements:
• Logo
• Name: P & K Hydro Excavation and Flushign
• Two phone numbers: Direct and Office
• Email address
• Website
• It should also have the name of the employee and their job title
• At the bottom of the card it should say (in a noticeable way): "24/7 Emergency Calls Welcome"
• The back of the card should have the following elements:
• "20 Years Experience"
• "A Canadian Family Run Business"
• A small maple-leaf logo that is in a similar style to the rest of the card/logos in the bottom right corner of the back of the card. (see attached)
Nice to have
• The card does not have to be a perfect rectangle. We are open to rounded corners or cut out elements.
• Also embossing, engraving, adding highlighted/glossy layers (spot glass?), or any other effect that will give the card a unique look/feel is more than welcome.
• We would love to have a card that stands out from others and is compelling to look at it, so we are happy to incorporate any sort of modern printing technology to bring out the design.
• Please feel encouraged to be creative and design something unique, especially for this industry.
• Our dream would be if a Scandinavian architect were to go into the construction business and design this business card ;)
Should not have
• Photographs

```html
<!DOCTYPE html>
<html lang="en">
<head>
<meta charset="utf-8">
<title>P &amp; K Hydro Excavation and Flushign – Business Card</title>
<link rel="stylesheet" href="https://fonts.googleapis.com/css2?family=Roboto:wght@400;500;700;900&display=swap">
<style>
  :root {
    --backdrop: #ece9e3;
    --navy: #2b2673;
    --navy-deep: #231f63;
    --white: #ffffff;
    --cyan: #3ab7ec;
    --yellow: #f2ec1a;
    --green: #1f8a3c;
    --green-dark: #16702f;
  }
  * { margin: 0; padding: 0; box-sizing: border-box; }
  html, body {
    width: 1200px; height: 900px; overflow: hidden;
    background: var(--backdrop);
    font-family: "Roboto", Arial, sans-serif;
  }
  .sheet {
    width: 1200px; height: 900px;
    display: flex; align-items: center; justify-content: center; gap: 40px;
  }
  .card {
    position: relative;
    width: 540px; height: 309px;
    border-radius: 22px;
    overflow: hidden;
    box-shadow: 0 10px 28px rgba(0,0,0,.18);
  }

  /* Front */
  .card-front { background: var(--navy); color: var(--white); }
  .brand-mark {
    position: absolute; left: 40px; top: 104px;
    display: flex; align-items: center; gap: 12px;
  }
  .brand-dot { width: 56px; height: 56px; border-radius: 50%; background: var(--white); }
  .brand-name { font-weight: 700; font-size: 30px; color: var(--white); letter-spacing: .5px; }
  .divider {
    position: absolute; left: 226px; top: 48px; width: 1px; height: 190px;
    background: rgba(255,255,255,.7);
  }
  .contact { position: absolute; left: 252px; top: 46px; }
  .person-name { font-size: 24px; font-weight: 500; line-height: 1.1; }
  .person-title { font-size: 14px; color: var(--cyan); margin-bottom: 10px; }
  .address { font-size: 13px; line-height: 1.35; margin-bottom: 6px; }
  .contact-line {
    display: flex; align-items: center; gap: 7px;
    font-size: 13px; line-height: 1.5;
  }
  .contact-icon {
    width: 12px; height: 12px; border-radius: 2px; background: var(--white);
    display: inline-flex; align-items: center; justify-content: center; flex: none;
  }
  .contact-icon svg { width: 8px; height: 8px; fill: var(--navy); }
  .emergency {
    position: absolute; right: 26px; bottom: 18px;
    font-size: 11px; letter-spacing: .2px;
  }

  /* Back */
  .card-back { background: var(--yellow); }
  .back-band {
    position: absolute; left: 0; right: 0; bottom: 0; height: 40px;
    background: var(--green);
    display: flex; align-items: center; justify-content: space-between;
    padding: 0 26px 0 150px;
  }
  .tagline { font-weight: 700; font-size: 13px; letter-spacing: 1px; color: var(--yellow); text-transform: uppercase; }
  .leaf-spot { width: 14px; height: 14px; background: var(--green-dark); border: 2px solid var(--yellow); transform: rotate(45deg); }
  .experience-tab {
    position: absolute; left: 0; bottom: 40px; width: 130px; height: 34px;
    background: var(--green-dark);
    clip-path: polygon(0 0, 88% 0, 100% 100%, 0 100%);
    display: flex; align-items: center; padding-left: 14px;
    font-weight: 700; font-size: 10px; letter-spacing: .8px; color: var(--yellow);
  }
  .back-brand {
    position: absolute; left: 150px; top: 70px;
    display: flex; align-items: center; gap: 14px;
  }
  .back-dot { width: 52px; height: 52px; border-radius: 50%; background: var(--green); flex: none; }
  .back-name {
    font-weight: 900; font-size: 22px; line-height: 1.15; color: var(--green);
    text-transform: uppercase; letter-spacing: .5px;
  }
</style>
</head>
<body>
<main class="sheet">

  <section class="card card-front" aria-label="Card front">
    <div class="brand-mark">
      <span class="brand-dot"></span>
      <span class="brand-name">P &amp; K</span>
    </div>
    <div class="divider"></div>
    <div class="contact">
      <p class="person-name">Evan Miller</p>
      <p class="person-title">Manager</p>
      <p class="address">250 Ridge Road, Unit 4<br>City, State, Zip Code</p>
      <p class="contact-line"><span class="contact-icon"><svg viewBox="0 0 10 10"><path d="M2 1h2l1 2-1 1a5 5 0 0 0 2 2l1-1 2 1v2a1 1 0 0 1-1 1A7 7 0 0 1 1 2a1 1 0 0 1 1-1z"/></svg></span>0781-5520-3194</p>
      <p class="contact-line"><span class="contact-icon"><svg viewBox="0 0 10 10"><path d="M2 1h2l1 2-1 1a5 5 0 0 0 2 2l1-1 2 1v2a1 1 0 0 1-1 1A7 7 0 0 1 1 2a1 1 0 0 1 1-1z"/></svg></span>0733-6408-2917</p>
      <p class="contact-line"><span class="contact-icon"><svg viewBox="0 0 10 10"><path d="M1 2h8v6H1z M1 2l4 3 4-3" fill="none" stroke="#2b2673" stroke-width="1.2"/></svg></span>emiller@mailbox.com</p>
      <p class="contact-line"><span class="contact-icon"><svg viewBox="0 0 10 10"><circle cx="5" cy="5" r="3.8" fill="none" stroke="#2b2673" stroke-width="1.2"/><path d="M1 5h8" stroke="#2b2673" stroke-width="1"/></svg></span>pkhydroexcavation.com</p>
    </div>
    <p class="emergency">24/7 Emergency Calls Welcome</p>
  </section>

  <section class="card card-back" aria-label="Card back">
    <div class="back-brand">
      <span class="back-dot"></span>
      <p class="back-name">P &amp; K Hydro<br>Excavation and Flushign</p>
    </div>
    <div class="experience-tab">20 YEARS EXPERIENCE</div>
    <div class="back-band">
      <span class="tagline">A Canadian Family Run Business</span>
      <span class="leaf-spot"></span>
    </div>
  </section>

</main>
</body>
</html>
```